Coffee Bag Label design for Australian Firefighter brand

I need a label for coffee bags. Front and back. We are based in Australia and aimed at Firefighters and First responders. I will have three size available. 250g, 500g and 1kg. So if we can use the same label that would be great. maybe a check box option at the bottom with the three sizes.
I really like the design for Lantern Roastworks (see attached), so I'm hoping for something along the same lines. replacing the images with firefighter axe, hose, halagan tool, cutting gear etc
I would like to include 'Firefighter founded" on the front, as well as 'Copper Ridge Blend'. Roasted med-dark on the Sunshine Coast, QLD
On the back I need space for a qr code with an arrow pointing to it with handwritten font 'how're you travelling? Free, confidential wellness check in'
and the text;
Coffee without the b.s.
This ain’t the sort of coffee for your average piccolo drinking, man-bun enthusiast. No fancy rose petal and unicorn pube infusions here. Just consistently great coffee that shows up, for those who show up. Firefighter founded and built with the Australian First Responder in mind.
Your life is complicated enough. Your coffee shouldn’t be.
For more, go to brasskettleroasters.com.au or scan the QR code for a free, fast, confidential mental wellness check-in and useful resources.
These will be printed as sticker lables to go on kraft black coffee bags to begin with. Please see attached bag example and logo for use.
Australian Firefighters and First responders

```html
<!DOCTYPE html>
<html lang="en">
<head>
<meta charset="utf-8">
<title>Ember Watch Coffee Co – Copper Ridge Blend Label</title>
<link rel="stylesheet" href="https://fonts.googleapis.com/css2?family=Barlow+Condensed:wght@300;400;600;700&display=swap">
<style>
  :root {
    --kraft-black: #2a2929;
    --chalk: #e4e2dd;
    --chalk-soft: #cfccc6;
    --alarm-red: #c2343b;
    --art-tone: #4a4947;
  }
  * { box-sizing: border-box; margin: 0; padding: 0; }
  html, body {
    width: 1091px;
    height: 1200px;
    overflow: hidden;
    background: var(--kraft-black);
  }
  .label {
    position: relative;
    width: 1091px;
    height: 1200px;
    background: var(--kraft-black);
    color: var(--chalk);
    font-family: "Barlow Condensed", "Arial Narrow", sans-serif;
  }
  .brand {
    position: absolute;
    top: 150px;
    left: 0;
    width: 100%;
    display: flex;
    justify-content: center;
    align-items: center;
    gap: 16px;
  }
  .brand-name {
    font-size: 54px;
    font-weight: 700;
    letter-spacing: 2px;
    text-transform: uppercase;
    color: var(--chalk);
  }
  .brand-dot {
    width: 30px;
    height: 30px;
    border-radius: 50%;
    background: var(--alarm-red);
  }
  .tool-illustration {
    position: absolute;
    top: 345px;
    left: 205px;
    width: 690px;
    height: 420px;
    background: radial-gradient(ellipse at center, #54524f 0%, var(--art-tone) 55%, #3a3938 100%);
    border-radius: 6px;
  }
  .product-info {
    position: absolute;
    top: 800px;
    left: 0;
    width: 100%;
    text-align: center;
  }
  .founded {
    font-size: 58px;
    font-weight: 700;
    letter-spacing: 1px;
    line-height: 1;
    text-transform: uppercase;
  }
  .blend {
    margin-top: 8px;
    font-size: 36px;
    font-weight: 600;
    letter-spacing: 0.5px;
    text-transform: uppercase;
    color: var(--alarm-red);
    line-height: 1;
  }
  .rule {
    width: 300px;
    height: 2px;
    margin: 18px auto 16px;
    background: var(--chalk-soft);
  }
  .roast {
    font-size: 31px;
    font-weight: 300;
    text-transform: uppercase;
    color: var(--chalk-soft);
    line-height: 1.1;
  }
  .origin {
    font-size: 34px;
    font-weight: 600;
    text-transform: uppercase;
    line-height: 1.1;
  }
  .size-picker {
    position: absolute;
    top: 960px;
    left: 850px;
    width: 120px;
    text-align: center;
  }
  .size-picker svg { display: block; margin: 0 auto 6px; }
  .size-list {
    font-size: 17px;
    font-weight: 600;
    letter-spacing: 0.5px;
    color: var(--chalk);
  }
</style>
</head>
<body>
  <main class="label">
    <header class="brand">
      <span class="brand-name">Ember Watch Coffee Co</span>
      <span class="brand-dot"></span>
    </header>

    <div class="tool-illustration" role="img" aria-label="Chalk-white illustrations of firefighting gear: hydrant, axe, halligan hook, megaphone, extinguisher, hose nozzle, traffic cone, flame, fire department badge and shovel"></div>

    <section class="product-info">
      <h1 class="founded">Firefighter Founded</h1>
      <h2 class="blend">Copper Ridge Blend</h2>
      <div class="rule"></div>
      <p class="roast">Roasted Med-Dark</p>
      <p class="origin">On the Sunshine Coast, QLD</p>
    </section>

    <aside class="size-picker">
      <svg width="110" height="42" viewBox="0 0 110 42" aria-hidden="true">
        <g fill="none" stroke="#e4e2dd" stroke-width="1.5">
          <rect x="2" y="20" width="106" height="18"/>
          <line x1="28.5" y1="20" x2="28.5" y2="38"/>
          <line x1="55" y1="20" x2="55" y2="38"/>
          <line x1="81.5" y1="20" x2="81.5" y2="38"/>
        </g>
        <path d="M44 22 L54 34 L74 4" fill="none" stroke="#e4e2dd" stroke-width="4" stroke-linecap="round" stroke-linejoin="round"/>
      </svg>
      <p class="size-list">250G | 500G | 1KG</p>
    </aside>
  </main>
</body>
</html>
```